Ringwell Lookup - Web design / template design

Hello,

I need a design for my existing site. I already have a logo that I want to use, which you can find on my site ( I can also provide different formats / larger versions ).

Please see http://www.ringwelllookup.example for details of the site.

What I need are pages with sections that can be edited, so for example, I need basic table / div content sections that I can place in the members area that can contain whatever custom content I need to put in them without the table / div design getting stretched out or skewed.

The main page, basically needs to have all of the content on the current page or room for it at least should I want to add it.

You can also see ww2.ringwelllookup.example with more info ( not a live site and me trying my best to do something, but I'm just not good at design :)

The site content for the most part needs to be actual text, rather than text on images. I will need to change this content and have it indexed by search engines, if you want, you can just put filler text in. There are exceptions of course, like maybe on the main page, if there are boxes with some static image text, that is fine.

Target Market(s)

Telephony, phone service providers, phone system users

Industry/Entity Type

It Service

Requirements
Must have
• Dynamic content capabilities.

Logo colors implemented in the site in some way.

Easy navigation ( tabs at the top are good or whatever you think ).

I will have the following sections:

1. Home
2. About us ( company info ).
3. How to / Help
4. Pricing
5. Support section.
6. Contact section
7. Singup section
8. Members section

I would like the main page to be more image / wow factor and the other pages really just need to be basic layout and places to put tables or divs with content in them. Table or div header images are for titles are ok as long as I can edit them.

Nice to have
• Sign up button placed somewhere.

Twitter / Facebook / LinkedIn buttons

Should not have
• Flash or all page content in static images.

```html
<!DOCTYPE html>
<html lang="en">
<head>
<meta charset="utf-8">
<title>About Us – Ringwell Lookup</title>
<link rel="stylesheet" href="https://fonts.googleapis.com/css2?family=Arimo:wght@400;700&display=swap">
<style>
  :root {
    --black: #000000;
    --white: #ffffff;
    --brand-blue: #1a56a6;
    --heading-blue: #0d4d9c;
    --nav-green-top: #3fae1c;
    --nav-green-bottom: #1f8a07;
    --nav-divider: #62c43c;
    --text: #111111;
    --footer-text: #8a8a8a;
    --photo-light: #e7eef5;
    --photo-mid: #c9d6e2;
    --photo-warm: #d9b89e;
    --arc-blue: #2f7fd1;
  }
  * { margin: 0; padding: 0; box-sizing: border-box; }
  html, body { width: 1200px; height: 818px; overflow: hidden; background: var(--white); }
  body { font-family: "Arimo", Arial, sans-serif; color: var(--text); position: relative; }

  .top-bar { position: absolute; left: 0; top: 0; width: 1200px; height: 78px; background: var(--black); }
  .account-links { position: absolute; right: 86px; top: 26px; height: 36px; display: flex; list-style: none; }
  .account-links li { border-left: 1px solid #555; border-right: 1px solid #555; margin-left: -1px; }
  .account-links a { display: block; padding: 0 29px; line-height: 36px; color: var(--white); font-size: 14px; letter-spacing: 0.5px; text-decoration: none; }

  .masthead { position: absolute; left: 87px; top: 78px; width: 1024px; height: 265px; background: var(--white); }
  .brand { position: absolute; left: 32px; top: 112px; display: flex; align-items: center; gap: 10px; }
  .brand-dot { width: 16px; height: 16px; border-radius: 50%; background: var(--brand-blue); }
  .brand-name { font-size: 32px; font-weight: 700; color: var(--brand-blue); letter-spacing: -0.5px; }
  .hero { position: absolute; left: 300px; top: 0; width: 724px; height: 265px; }

  .main-nav { position: absolute; left: 87px; top: 343px; width: 1024px; height: 50px;
    background: linear-gradient(var(--nav-green-top), var(--nav-green-bottom)); display: flex; list-style: none; }
  .main-nav li { flex: 1; text-align: center; border-left: 1px solid var(--nav-divider); }
  .main-nav li:first-child { border-left: none; }
  .main-nav a { display: block; line-height: 50px; color: var(--white); font-size: 15px; letter-spacing: 1px; text-decoration: none; }

  .page-title { position: absolute; left: 129px; top: 435px; font-size: 29px; font-weight: 700; color: var(--heading-blue); }
  .content { position: absolute; left: 109px; top: 503px; width: 980px; display: flex; gap: 44px; }
  .content-block { width: 468px; }
  .content-block p { font-size: 14.2px; line-height: 17.5px; margin-bottom: 15px; text-align: justify; }

  .site-footer { position: absolute; left: 0; top: 775px; width: 1200px; height: 43px; background: var(--black); text-align: center; }
  .site-footer p { line-height: 43px; font-size: 10px; color: var(--footer-text); }
</style>
</head>
<body>
  <header class="top-bar">
    <ul class="account-links">
      <li><a href="#">Register</a></li>
      <li><a href="#">Log In</a></li>
    </ul>
  </header>

  <section class="masthead">
    <div class="brand">
      <span class="brand-dot"></span>
      <span class="brand-name">Ringwell Lookup</span>
    </div>
    <svg class="hero" viewBox="0 0 724 265" role="img" aria-label="Photo of a smiling support agent wearing a headset">
      <defs>
        <linearGradient id="heroFill" x1="0" y1="0" x2="1" y2="0">
          <stop offset="0" stop-color="var(--photo-mid)"/>
          <stop offset="0.4" stop-color="var(--photo-warm)"/>
          <stop offset="0.75" stop-color="var(--photo-light)"/>
          <stop offset="1" stop-color="var(--photo-mid)"/>
        </linearGradient>
      </defs>
      <path d="M40 0 H724 V265 H28 Q80 140 40 0 Z" fill="url(#heroFill)"/>
      <path d="M40 0 Q80 140 28 265" fill="none" stroke="var(--arc-blue)" stroke-width="5"/>
    </svg>
  </section>

  <nav>
    <ul class="main-nav">
      <li><a href="#">Home</a></li>
      <li><a href="#">CNAM Help</a></li>
      <li><a href="#">Pricing</a></li>
      <li><a href="#">Support</a></li>
      <li><a href="#">Contact Us</a></li>
    </ul>
  </nav>

  <h1 class="page-title">About Us</h1>

  <main class="content">
    <article class="content-block">
      <p>CNAM is a database of caller names used to identify the name of a caller when receiving an inbound call from the United States or Canada.</p>
      <p>The name of a caller is determined by searching a database for a name associated with the phone number of the calling party. You likely receive caller ID name produced by a lookup into a CNAM database on your land line phone service at home.</p>
      <p>Since the process of matching the caller's number to a CNAM database requires additional hardware and maitenence, it's likely that your VoIP provider does not provide caller ID name services with your inbound voice over IP calls, so you see only the number of the caller, preventing you from identifying the caller before you answer your calls.</p>
      <p>That's where RingwellLookup.example comes in!</p>
    </article>
    <article class="content-block">
      <p>CNAM is a database of caller names used to identify the name of a caller when receiving an inbound call from the United States or Canada.</p>
      <p>The name of a caller is determined by searching a database for a name associated with the phone number of the calling party. You likely receive caller ID name produced by a lookup into a CNAM database on your land line phone service at home.</p>
      <p>Since the process of matching the caller's number to a CNAM database requires additional hardware and maitenence, it's likely that your VoIP provider does not provide caller ID name services with your inbound voice over IP calls, so you see only the number of the caller, preventing you from identifying the caller before you answer your calls.</p>
      <p>That's where RingwellLookup.example comes in!</p>
    </article>
  </main>

  <footer class="site-footer">
    <p>Copyright Ringwell Lookup 2011.</p>
  </footer>
</body>
</html>
```